Design few pages for professional development app

I need a website design for a prototype project. The goal of the project is to prototype a few basic screens for a professional development application.

The final design should be clean, modern, and appeal to a professional millenial clientele.The designs have been wireframed (see attached), and we'd like these wireframes converted to design files.

Here is the list of goals and tasks that correspond to the design: https://sheets.plorvane.com/tables/d/7qWmK84x9PLzn3oTcB2vEaRyhUDs-kfNJ52tqXyMHw/edit?usp=sharing

Number of Pages Required

5+ page

Font styles to use
Serif
Sans Serif

Colors

Designer to choose colors to be used in the design.

Requirements
Nice to have
• Uses Google Material Design, Bootstrap, or another framework

```html
<!DOCTYPE html>
<html lang="en">
<head>
<meta charset="utf-8">
<title>Ascendly — Main Goals</title>
<link href="https://fonts.googleapis.com/css2?family=Nunito:wght@400;600;700&display=swap" rel="stylesheet">
<style>
  :root {
    --bg: #ebf0f5;
    --surface: #ffffff;
    --ink: #3d4a5a;
    --ink-soft: #4a5563;
    --brand: #3d4a5a;
    --primary: #1a73d4;
    --check: #e6f1fa;
    --search-bg: #dde3ea;
    --teal-bg: #b9e3e6;
    --teal: #1a9aa6;
    --peach-bg: #fcd9be;
    --orange: #f07c1c;
    --green-bg: #d5e6cc;
    --green: #5a9a35;
    --sand-bg: #fde4bd;
    --amber: #f29b1c;
  }
  * { box-sizing: border-box; margin: 0; padding: 0; }
  html, body { width: 1200px; height: 675px; overflow: hidden; }
  body { background: var(--bg); font-family: "Nunito", sans-serif; color: var(--ink); position: relative; }

  .topbar { position: absolute; left: 0; top: 0; width: 1200px; height: 50px; background: var(--surface); }
  .brand { position: absolute; left: 24px; top: 14px; font-size: 15px; font-weight: 700; color: var(--brand); }
  .search-btn { position: absolute; left: 1022px; top: 10px; width: 30px; height: 30px; border-radius: 5px; background: var(--search-bg); display: flex; align-items: center; justify-content: center; }
  .user { position: absolute; left: 1071px; top: 10px; display: flex; align-items: center; gap: 8px; }
  .avatar { width: 30px; height: 30px; border-radius: 5px; background: linear-gradient(135deg, #6b3b25, #d9a27c); }
  .user-name { font-size: 11px; font-weight: 600; color: var(--ink-soft); }

  .intro { position: absolute; left: 253px; top: 104px; width: 230px; }
  .intro h1 { font-size: 31px; line-height: 38px; font-weight: 700; color: var(--ink); }
  .intro p { margin-top: 17px; font-size: 11px; line-height: 17px; color: var(--ink-soft); }
  .hero-art { position: absolute; left: 269px; top: 247px; width: 190px; height: 191px; border-radius: 50%; background: radial-gradient(circle at 55% 50%, #2f7ede 0%, #7fb0ea 35%, #f9c84a 60%, rgba(235,240,245,0) 72%); }

  .goals { position: absolute; left: 551px; top: 112.5px; width: 337.5px; list-style: none; }
  .goal { height: 61px; background: var(--surface); border-radius: 5px; margin-bottom: 12.5px; display: flex; align-items: center; padding-left: 15px; }
  .goal-check { width: 24px; height: 24px; border-radius: 5px; background: var(--check); }
  .goal-icon { width: 42.5px; height: 42.5px; border-radius: 4px; margin-left: 18px; display: flex; align-items: center; justify-content: center; }
  .goal-label { margin-left: 11px; font-size: 14px; font-weight: 600; color: var(--ink); }
  .icon-network { background: var(--teal-bg); }
  .icon-branding { background: var(--peach-bg); }
  .icon-promotion { background: var(--green-bg); }
  .icon-leader { background: var(--sand-bg); }

  .cta { position: absolute; left: 712.5px; top: 417.5px; width: 176px; height: 31px; border-radius: 5px; background: var(--primary); color: #fff; font-family: "Nunito", sans-serif; font-size: 10.6px; font-weight: 700; border: 0; }
</style>
</head>
<body>
  <header class="topbar">
    <div class="brand">Ascendly</div>
    <div class="search-btn">
      <svg width="14" height="14" viewBox="0 0 24 24" fill="none" stroke="#6b7684" stroke-width="2.6" stroke-linecap="round"><circle cx="10" cy="10" r="6.5"/><line x1="15" y1="15" x2="21" y2="21"/></svg>
    </div>
    <div class="user">
      <div class="avatar" role="img" aria-label="Profile photo of the signed-in user"></div>
      <span class="user-name">Nora Vale</span>
    </div>
  </header>

  <section class="intro">
    <h1>What Are Your Main Goals?</h1>
    <p>Tell us what you would like to achieve with Ascendly.</p>
  </section>
  <div class="hero-art" role="img" aria-label="Illustration of a businessman running through a finish ribbon holding a flag"></div>

  <ul class="goals">
    <li class="goal">
      <span class="goal-check"></span>
      <span class="goal-icon icon-network">
        <svg width="20" height="20" viewBox="0 0 24 24" fill="none" stroke="var(--teal)" stroke-width="1.8" stroke-linejoin="round" stroke-linecap="round"><path d="M3 3c2 2 5 3 9 3s7-1 9-3"/><path d="M10 6l-1 3 3 2 3-2-1-3"/><path d="M10.5 10l-1 9 2.5 2 2.5-2-1-9"/></svg>
      </span>
      <span class="goal-label">Build my Network</span>
    </li>
    <li class="goal">
      <span class="goal-check"></span>
      <span class="goal-icon icon-branding">
        <svg width="20" height="20" viewBox="0 0 24 24" fill="none" stroke="var(--orange)" stroke-width="1.8" stroke-linejoin="round"><circle cx="12" cy="9" r="4.5"/><circle cx="7.5" cy="4.5" r="1.8" fill="var(--orange)"/><circle cx="16.5" cy="4.5" r="1.8" fill="var(--orange)"/><path d="M4 21l3-7h10l3 7z"/></svg>
      </span>
      <span class="goal-label">Personal Branding</span>
    </li>
    <li class="goal">
      <span class="goal-check"></span>
      <span class="goal-icon icon-promotion">
        <svg width="20" height="20" viewBox="0 0 24 24" fill="none" stroke="var(--green)" stroke-width="1.8" stroke-linejoin="round"><rect x="3" y="8" width="18" height="4"/><rect x="5" y="12" width="14" height="9"/><line x1="12" y1="8" x2="12" y2="21"/><path d="M12 8c-2-5-6-4-5-1 1 1 5 1 5 1zM12 8c2-5 6-4 5-1-1 1-5 1-5 1z"/></svg>
      </span>
      <span class="goal-label">Get a Promotion</span>
    </li>
    <li class="goal">
      <span class="goal-check"></span>
      <span class="goal-icon icon-leader">
        <svg width="20" height="20" viewBox="0 0 24 24" fill="none" stroke="var(--amber)" stroke-width="1.8" stroke-linejoin="round" stroke-linecap="round"><path d="M3 10h5l9-5v14l-9-5H3z"/><path d="M5 14l2 6h3l-2-6"/><path d="M20 10v4"/></svg>
      </span>
      <span class="goal-label">Be a Better Leader</span>
    </li>
  </ul>

  <button class="cta" type="button">See My Personalized List</button>
</body>
</html>
```